'Quarrystone Co' Business Cards

Quarrystone Co is a clothing company geared toward people in the mining industry who are crushing it (literally) We need a design for a business card that has 'QS' similar to the layout of the inspo photo below. Rock textures and maybe some rock dust (see GIF). I Included SVG of our circle logo but not sure how to include without it being boring, would like some ideas. Front should say 'Quarrystone Co.' (and 'clothing' in smaller letters below) Back should have our webpage 'quarrystoneco.ca' our email 'info@quarrystoneco.ca' plus a FB and IG icon

```html
<!DOCTYPE html>
<html lang="en">
<head>
<meta charset="utf-8">
<title>Quarrystone Co. Business Cards</title>
<link rel="stylesheet" href="https://fonts.googleapis.com/css2?family=Open+Sans:wght@400;700;800&display=swap">
<style>
  :root {
    --page: #e9e9e9;
    --ink: #111111;
    --ink-soft: #2b2b2b;
    --stone-light-a: #d2d2d0;
    --stone-light-b: #b9b9b7;
    --stone-dark-a: #7a7a7a;
    --stone-dark-b: #4f4f4f;
    --card-shadow: rgba(0, 0, 0, 0.28);
  }
  * { box-sizing: border-box; margin: 0; padding: 0; }
  html, body {
    width: 1200px;
    height: 1200px;
    overflow: hidden;
    background: var(--page);
    font-family: "Open Sans", Arial, sans-serif;
    color: var(--ink);
  }
  .sheet {
    position: relative;
    width: 1200px;
    height: 1200px;
  }
  .card {
    position: absolute;
    left: 150px;
    width: 900px;
    height: 514px;
    overflow: hidden;
    box-shadow: 0 14px 34px var(--card-shadow);
  }
  .card--back { top: 48px; }
  .card--front { top: 636px; }

  .card__stone {
    position: absolute;
    inset: 0;
  }
  .card--back .card__stone {
    background: linear-gradient(160deg, var(--stone-light-a) 0%, var(--stone-light-b) 55%, var(--stone-light-a) 100%);
  }
  .card--front .card__stone {
    background: linear-gradient(165deg, var(--stone-dark-a) 0%, var(--stone-dark-b) 50%, var(--stone-dark-a) 100%);
  }

  .brand {
    position: absolute;
    display: flex;
    align-items: center;
    gap: 18px;
    color: var(--ink);
  }
  .brand__dot {
    width: 58px;
    height: 58px;
    border-radius: 50%;
    background: var(--ink);
    flex: none;
  }
  .brand__name {
    font-weight: 800;
    font-size: 78px;
    letter-spacing: 1px;
    line-height: 1;
    text-transform: uppercase;
  }
  .card--back .brand { left: 90px; top: 150px; }
  .card--front .brand { left: 70px; top: 150px; }
  .card--front .brand__name { font-size: 82px; }

  .contact {
    position: absolute;
    left: 330px;
    top: 300px;
    list-style: none;
    font-size: 24px;
    color: var(--ink-soft);
    line-height: 1.45;
  }
  .contact__item {
    display: flex;
    align-items: center;
    gap: 12px;
  }
  .contact__icon {
    width: 22px;
    height: 22px;
    flex: none;
  }

  .tagline {
    position: absolute;
    left: 110px;
    top: 320px;
    font-weight: 700;
    font-size: 40px;
    color: var(--ink);
  }
</style>
</head>
<body>
<main class="sheet">

  <section class="card card--back" aria-label="Business card, back">
    <div class="card__stone" role="img" aria-label="Light grey split-rock texture with a halftone dot fade in the upper right"></div>
    <div class="brand">
      <span class="brand__dot"></span>
      <span class="brand__name">Quarrystone</span>
    </div>
    <ul class="contact">
      <li class="contact__item">
        <svg class="contact__icon" viewBox="0 0 24 24" fill="none" stroke="#2b2b2b" stroke-width="1.8">
          <circle cx="12" cy="12" r="9.5"/>
          <ellipse cx="12" cy="12" rx="4.2" ry="9.5"/>
          <line x1="2.5" y1="12" x2="21.5" y2="12"/>
          <path d="M4.5 7h15M4.5 17h15"/>
        </svg>
        <span>www.quarrystoneco.ca</span>
      </li>
      <li class="contact__item">
        <svg class="contact__icon" viewBox="0 0 24 24">
          <rect x="2" y="5" width="20" height="14" fill="#2b2b2b"/>
          <path d="M2.5 5.5 12 13l9.5-7.5" fill="none" stroke="#e0e0e0" stroke-width="1.5"/>
        </svg>
        <span>info@quarrystoneco.ca</span>
      </li>
    </ul>
  </section>

  <section class="card card--front" aria-label="Business card, front">
    <div class="card__stone" role="img" aria-label="Dark grey granite rock texture with a faint halftone dot fade in the upper left"></div>
    <div class="brand">
      <span class="brand__dot"></span>
      <span class="brand__name">Quarrystone</span>
    </div>
    <p class="tagline">Quarrystone Co. clothing</p>
  </section>

</main>
</body>
</html>
```